Real estate company needing card designed to specifications

WB ESTATES The company logo on front of the card to be split between top and bottom per below business card. I would see this going all the way across the card or at least most of it.
Under the writing in the top right side add PARTNERS.

Front of the card in the middle it will be Owen Marsh | Director
and on separate card Daniel Marsh | Director

Back of the card centred will be:

Wbestates.com.au
owen@wbestates.com.au or daniel@wbestates.com.au
0413 527 908 or 0409 218 337
Level 14, 85 Carrow Street
Sydney NSW 2000

Card:
Soft grey carbon fibre look.

Writing to be in royal blue.

Writing font to be ‘Mirabel’ style attached. This is a very fine font used on landing page of:
https://www.dravemotors.example/anton-dravemark/

The company logo to be split between top and bottom per attached image

Target Market(s)

These cards are to hand out to clients and inspections.

Industry/Entity Type

Real Estate Agent

Contact Information for Business Card

Wbestates.com.au
Sydney NSW 2000

Card:

Logo Text

WB ESTATES

Font styles to use
Other font styles liked:
• uploaded Mirabel file font.

Colors

Designer to choose colors to be used in the design.

```html
<!DOCTYPE html>
<html lang="en">
<head>
<meta charset="utf-8">
<title>WB Estates – Business Card Back</title>
<link rel="stylesheet" href="https://fonts.googleapis.com/css2?family=Source+Sans+3:wght@300&display=swap">
<style>
  :root {
    --page-bg: #ffffff;
    --card-grey-light: #aeaeb0;
    --card-grey-mid: #9a9a9c;
    --card-grey-dark: #858587;
    --ink-royal: #12214f;
  }
  html, body {
    margin: 0;
    padding: 0;
    width: 1200px;
    height: 1200px;
    overflow: hidden;
    background: var(--page-bg);
  }
  .canvas {
    position: relative;
    width: 1200px;
    height: 1200px;
  }
  .card-back {
    position: absolute;
    left: 180px;
    top: 360px;
    width: 840px;
    height: 480px;
    overflow: hidden;
  }
  .card-texture {
    position: absolute;
    inset: 0;
    width: 100%;
    height: 100%;
    display: block;
  }
  .contact-block {
    position: absolute;
    inset: 0;
    display: flex;
    flex-direction: column;
    justify-content: center;
    align-items: center;
    padding-right: 22px;
    padding-top: 2px;
    box-sizing: border-box;
    font-family: "Source Sans 3", sans-serif;
    font-weight: 300;
    font-size: 36px;
    line-height: 50px;
    color: var(--ink-royal);
    text-align: center;
  }
  .contact-line {
    margin: 0;
    white-space: nowrap;
  }
</style>
</head>
<body>
  <main class="canvas">
    <section class="card-back">
      <svg class="card-texture" viewBox="0 0 840 480" preserveAspectRatio="none" role="img" aria-label="Soft grey carbon fibre weave texture">
        <defs>
          <linearGradient id="weave-tone" x1="0" y1="0" x2="1" y2="1">
            <stop offset="0" stop-color="var(--card-grey-light)"/>
            <stop offset="0.5" stop-color="var(--card-grey-mid)"/>
            <stop offset="1" stop-color="var(--card-grey-dark)"/>
          </linearGradient>
        </defs>
        <rect width="840" height="480" fill="url(#weave-tone)"/>
      </svg>
      <div class="contact-block">
        <p class="contact-line website">Wbestates.com.au</p>
        <p class="contact-line email">owen@wbestates.com.au</p>
        <p class="contact-line phone">0413 527 908</p>
        <p class="contact-line street">Level 14, 85 Carrow Street</p>
        <p class="contact-line city">Sydney NSW 2000</p>
      </div>
    </section>
  </main>
</body>
</html>
```